Broschüre für externen Datenschutzpartner
Herzlichen Dank an KoLuxAr für die ausgezeichneten Arbeiten und das perfekte Ergebnis.
Zielgruppe
Korvento hat sich darauf spezialisiert, insbesondere kleine und mittelständische Unternehmen als externer Datenschutzpartner kontinuierlich zu betreuen und zu beraten. Durch neue Anforderungen – bereits heute durch die DS-GVO und zukünftig durch die EPVO – wird es zunehmend notwendig für Unternehmen, verstärkt externe Beratung mit entsprechendem Know-how in den Bereichen Datenschutz und IT-Sicherheit einzuholen. Denn der Schutz personenbezogener Daten sowie die geforderte Sicherheit haben durch die Gültigkeit der europaweit geltenden DS-GVO massiv an Bedeutung gewonnen. Dieser Trend wird durch die zunehmende Digitalisierung weiter zunehmen. Hier bieten wir ein breites Leistungsspektrum an.
Aufgabenstellung
Eine Broschüre als Vorlage ist beigefügt. (Brisalt-Info-NetzwerkAblauf.pdf) Es sollen ebenso alle relevanten Informationen auf die Seiten verteilt werden, ohne die Seiten zu überladen. Bei den Grafiken würden wir uns ähnliche Bilder (StockPhotos) wünschen. Die vorhandene CI der Korvento (www.korvento.de) soll dabei wieder zu erkennen sein.
Alle weiteren Informationen sind den beigefügten Dokumenten und der Website zu entnehmen. Die Broschüre soll das Präsentation dargestellt werden. zwischen 7-9 Seiten. Inhaltliche Fragen werden jederzeit beantwortet.

```html
<!DOCTYPE html>
<html lang="de">
<head>
<meta charset="utf-8">
<title>Korvento – Broschüre IT-Sicherheit &amp; Datenschutz</title>
<link href="https://fonts.googleapis.com/css2?family=Raleway:wght@300;400;600;700&family=Montserrat:wght@300;400;600&display=swap" rel="stylesheet">
<style>
:root{
  --green:#3aaa35;
  --green-dark:#2f8f2b;
  --charcoal:#555556;
  --grey:#8a8a8a;
  --grey-light:#e9e9e9;
  --paper:#ffffff;
  --stage:#d3d3d3;
  --text:#5a5a5a;
}
*{box-sizing:border-box;margin:0;padding:0}
html,body{width:1200px;height:3744px;overflow:hidden;background:var(--stage)}
body{position:relative;font-family:"Montserrat",sans-serif;color:var(--text)}
.page{position:absolute;left:270px;background:var(--paper);overflow:hidden}
.abs{position:absolute}
.photo{position:absolute;background:linear-gradient(160deg,#e4e7ec 0%,#9ea3aa 45%,#4d5257 75%,#2f6e2c 100%)}
.photo.office{background:linear-gradient(150deg,#cfdbe6 0%,#a9bccc 45%,#6f7f8d 100%)}
.h-section{font-family:"Raleway",sans-serif;font-weight:400;text-transform:uppercase;letter-spacing:.3px}
.h-section b{font-weight:700}
.body{font-size:7.4px;line-height:1.5}
.body p{margin-bottom:7px}
.logo-name{font-family:"Raleway",sans-serif;font-weight:600;color:var(--green);letter-spacing:-.5px;line-height:1}
.logo-sub{font-family:"Montserrat",sans-serif;font-size:9px;color:var(--charcoal);font-weight:600}
.logo-dot{display:inline-block;border-radius:50%;background:var(--green);vertical-align:middle}

/* Seite 1 – Titel */
.cover{top:58px;width:650px;height:456px;background:linear-gradient(90deg,#f3f3f3,#ffffff)}
.cover-band{left:0;top:318px;width:330px;height:138px;background:var(--charcoal)}
.cover-title{left:32px;top:345px;font-family:"Raleway",sans-serif;font-weight:400;font-size:30px;line-height:1.2;color:#fff}

/* Seite 2 – Konzept */
.concept{top:569px;width:650px;height:457px}
.concept-side{left:0;top:0;width:248px;height:457px;background:var(--green);color:#fff;padding:68px 32px 0 37px}
.concept-side .h-section{font-size:15px;margin-bottom:32px}
.concept-side .body{font-size:7px}
.concept-main{left:288px;top:278px;width:340px}
.cols{display:flex;gap:24px}
.cols .body{flex:1}

/* Seite 3 – Vorteile */
.benefits{top:1079px;width:670px;height:474px;background:linear-gradient(180deg,#fafafa,#efefef)}
.topbar{left:0;top:0;width:100%;height:9px;background:var(--green)}
.pill{position:absolute;width:212px;height:78px;border:2.5px solid var(--green);border-radius:40px;background:#fff;display:flex;align-items:center;padding:0 12px}
.pill .txt{flex:1;font-size:5.6px;line-height:1.35;color:var(--grey)}
.pill .ttl{font-family:"Raleway",sans-serif;font-weight:600;color:var(--green);font-size:11px;text-transform:uppercase;margin-bottom:3px}
.pill.left .txt{text-align:center}
.pill .ico{width:52px;height:52px;border-radius:50%;background:#e6e6e6;border:3px solid #fff;box-shadow:0 0 0 2.5px var(--green);display:flex;align-items:center;justify-content:center;flex:none}
.pill.left .ico{margin-left:8px}
.pill.right .ico{margin-right:10px}

/* Seite 4 – Prinzipien */
.principles{top:1604px;width:679px;height:479px}
.principles-band{left:0;top:0;width:679px;height:210px;background:var(--charcoal)}
.principles-title{left:0;top:82px;width:679px;text-align:center;color:#fff;font-family:"Raleway",sans-serif;font-size:22px;font-weight:400}
.pillar{position:absolute;top:160px;width:190px;text-align:center}
.pillar h3{font-family:"Raleway",sans-serif;font-weight:400;font-size:17px;line-height:1.15;color:var(--charcoal);text-transform:uppercase;margin:14px 0 20px}
.pillar .body{font-size:8.3px;line-height:1.55;padding:0 12px}
.pillar .lead{color:var(--green);font-weight:600}

/* Seite 5 – Kultur */
.culture{top:2131px;width:679px;height:477px}
.culture-side{left:415px;top:0;width:264px;height:477px;background:var(--green);color:#fff;padding:24px 30px 0 42px}
.culture-side .h-section{font-size:15px;margin-bottom:22px}

/* Seite 6 – Pakete */
.packages{top:2662px;width:681px;height:479px}
.packages-band{left:0;top:0;width:681px;height:280px;background:var(--green)}
.packages-title{left:0;top:160px;width:681px;text-align:center;color:#fff;font-family:"Raleway",sans-serif;font-size:22px}
.pack{position:absolute;top:258px;width:129px;text-align:center}
.price{width:56px;height:56px;margin:0 auto -10px;position:relative;z-index:2}
.pack-label{background:var(--grey);color:#fff;font-size:9.5px;font-family:"Raleway",sans-serif;padding:8px 0 4px;text-transform:uppercase}
.pack.xl .pack-label{background:var(--green)}
.pack-list{background:var(--grey-light);padding:8px 10px 10px;font-size:6px;text-transform:uppercase;color:#666}
.pack-list li{list-style:none;padding:3px 0;border-bottom:1px solid #d2d2d2}
.pack-list li:last-child{border-bottom:none}

/* Seite 7 – Zielgruppe */
.audience{top:3196px;width:681px;height:484px}
.audience-list{left:28px;top:84px;width:440px}
.audience-item{display:flex;gap:14px;align-items:flex-start;margin-bottom:22px;font-size:7.6px;line-height:1.5}
.audience-bottom{left:0;top:258px;width:681px;height:226px;background:var(--green);color:#fff;padding:20px 220px 0 30px}
.audience-bottom .h-section{font-size:15px;margin-bottom:18px}
.cta-tag{left:487px;top:24px;background:var(--grey);color:#fff;font-size:7px;padding:2px 6px;text-transform:uppercase}
.cta-phone{left:487px;top:38px;width:181px;height:24px;background:var(--charcoal);color:#fff;font-size:11px;display:flex;align-items:center;gap:8px;padding-left:24px}
</style>
</head>
<body>

<!-- Seite 1 -->
<section class="page cover">
  <div class="abs" style="left:28px;top:24px">
    <div class="logo-name" style="font-size:52px"><span class="logo-dot" style="width:12px;height:12px;margin-right:8px"></span>korvento</div>
    <div class="logo-sub" style="margin-left:28px;margin-top:2px">Professioneller Datenschutz für Unternehmen</div>
  </div>
  <svg class="abs" style="left:270px;top:-10px" width="400" height="480" viewBox="0 0 400 480">
    <defs>
      <linearGradient id="knight1" x1="0" y1="0" x2="1" y2="1">
        <stop offset="0" stop-color="#dfe2e7"/><stop offset=".5" stop-color="#6f7379"/><stop offset="1" stop-color="#2d6d2a"/>
      </linearGradient>
    </defs>
    <path d="M60 130 Q60 70 130 60 L300 60 Q370 60 400 90 L400 480 L240 480 Q120 420 80 330 Q60 280 60 230 Z" fill="url(#knight1)" stroke="var(--green)" stroke-width="14" role="img" aria-label="Foto: Ritter in Rüstung mit grünem Schild"/>
  </svg>
  <div class="abs cover-band"></div>
  <div class="abs cover-title">IT-SICHERHEIT &amp;<br>DATENSCHUTZ</div>
</section>

<!-- Seite 2 -->
<section class="page concept">
  <div class="abs concept-side">
    <h2 class="h-section">Unser <b style="font-weight:400">Konzept</b></h2>
    <div class="body">
      <p>Die Korvento GmbH &amp; Co. KG ist ein junges, dynamisches Beratungsunternehmen mit Sitz im Herzen von Düsseldorf. Korvento hat sich darauf spezialisiert, insbesondere kleine und mittelständische Unternehmen als externer Datenschutzpartner kontinuierlich zu betreuen und zu beraten.</p>
      <p>Durch neue Anforderungen – bereits heute durch die DS-GVO und zukünftig durch die EPVO – wird es zunehmend notwendig für Unternehmen, verstärkt externe Beratung mit entsprechendem Know-how in den Bereichen Datenschutz und IT-Sicherheit einzuholen.</p>
      <p>Denn der Schutz personenbezogener Daten sowie die geforderte Sicherheit haben durch die Gültigkeit der europaweit geltenden DS-GVO massiv an Bedeutung gewonnen. Dieser Trend wird durch die zunehmende Digitalisierung weiter zunehmen.</p>
      <p style="font-weight:600">HIER BIETEN WIR EIN BREITES LEISTUNGSSPEKTRUM AN.</p>
    </div>
  </div>
  <div class="photo" style="left:248px;top:22px;width:402px;height:228px" role="img" aria-label="Foto: Ritter mit grünem Schild und Schwert vor hellem Hintergrund"></div>
  <div class="abs concept-main">
    <h2 class="h-section" style="font-size:15px;color:var(--charcoal);margin-bottom:26px">Unsere Aufgaben</h2>
    <div class="cols">
      <div class="body">Als Anbieter für externen Datenschutz und IT-Sicherheit verfügt Korvento über eine hochwertige inhaltliche sowie technische Expertise und bildet damit das Fundament für die Einhaltung der DS-GVO und der zukünftigen EPVO in Unternehmen bis zu einer mittelständischen Größe. Wir helfen Ihnen dabei, die neue DS-GVO und die EPVO problemlos in Ihrem Unternehmen zu integrieren.</div>
      <div class="body"><p>Zudem beraten wir Sie fortlaufend, um eine pragmatische Umsetzung der Anforderungen im Bereich Datenschutz zu gewährleisten.</p><p>Dazu zählen auch <b>notwendige technische und organisatorische Maßnahmen.</b> Als externe Datenschutzbeauftragte bringen wir die nötige Expertise mit, um Ihr Unternehmen zu beraten.</p></div>
    </div>
  </div>
</section>

<!-- Seite 3 -->
<section class="page benefits">
  <div class="abs topbar"></div>
  <div class="abs" style="left:0;top:28px;width:670px;text-align:center">
    <div class="logo-name" style="font-size:30px"><span class="logo-dot" style="width:7px;height:7px;margin-right:5px"></span>korvento</div>
    <div class="logo-sub" style="font-size:5.5px">Professioneller Datenschutz für Unternehmen</div>
  </div>

  <div class="pill left" style="left:52px;top:84px"><div class="txt"><div class="ttl">Betreuung</div>Eine kontinuierliche Betreuung sehen wir als selbstverständlich an – nur so wird Ihr Unternehmen dauerhaft geschützt.</div>
    <div class="ico"><svg width="26" height="26" viewBox="0 0 26 26"><path d="M5 13a8 8 0 0 1 14-5M21 13a8 8 0 0 1-14 5" fill="none" stroke="#444" stroke-width="3"/><path d="M19 3v6h-6M7 23v-6h6" fill="none" stroke="#444" stroke-width="2.5"/></svg></div></div>
  <div class="pill right" style="left:410px;top:84px"><div class="ico"><svg width="24" height="28" viewBox="0 0 24 28"><circle cx="12" cy="10" r="8" fill="#444"/><circle cx="12" cy="10" r="3.5" fill="#e6e6e6"/><path d="M7 16l-3 10 4-2 3 3 1-8M17 16l3 10-4-2-3 3-1-8" fill="#444"/></svg></div>
    <div class="txt"><div class="ttl">Kompetenz</div>Datenschutz ist ein sehr umfassendes Thema und bereitet vielen Unternehmen Sorgen. Wir geben Ihnen klare Orientierung.</div></div>

  <div class="pill left" style="left:20px;top:212px;width:220px;height:66px"><div class="txt"><div class="ttl">Technologie</div>Zeit- und materialsparende Prozesse über unsere Kundenplattform sorgen für eine schnelle Umsetzung.</div>
    <div class="ico"><svg width="26" height="22" viewBox="0 0 26 22"><rect x="2" y="2" width="22" height="14" fill="none" stroke="#444" stroke-width="2.5"/><path d="M8 9l3 3 6-6" fill="none" stroke="#444" stroke-width="2.5"/><path d="M9 20h8M13 16v4" stroke="#444" stroke-width="2.5"/></svg></div></div>
  <div class="pill right" style="left:438px;top:212px;width:220px;height:66px"><div class="ico"><svg width="28" height="20" viewBox="0 0 28 20"><path d="M2 8l7-5 5 3 5-3 7 5-9 9-4-3-3 2Z" fill="#444"/></svg></div>
    <div class="txt"><div class="ttl">Partnerschaft</div>Die Formel für eine optimale Kundenbeziehung ist der Erfolg, der sich aus Vertrauen und Verständnis ergibt.</div></div>

  <svg class="abs" style="left:276px;top:188px" width="118" height="130" viewBox="0 0 118 130">
    <path d="M59 4 L110 22 L110 70 Q110 105 59 126 Q8 105 8 70 L8 22 Z" fill="#fff" stroke="var(--green)" stroke-width="5"/>
    <text x="59" y="50" text-anchor="middle" font-family="Raleway,sans-serif" font-size="14" fill="#666">IHRE</text>
    <text x="59" y="68" text-anchor="middle" font-family="Raleway,sans-serif" font-size="14" fill="#666">VORTEILE</text>
    <line x1="47" y1="80" x2="71" y2="80" stroke="var(--green)" stroke-width="2.5"/>
  </svg>

  <div class="pill left" style="left:52px;top:340px"><div class="txt"><div class="ttl">Transparenz</div>Durch unsere individuellen Leistungspakete bezahlen Sie nur, was Sie brauchen – fair und ohne versteckte Kosten.</div>
    <div class="ico"><svg width="24" height="24" viewBox="0 0 24 24"><circle cx="14" cy="10" r="7" fill="none" stroke="#444" stroke-width="3"/><path d="M9 15l-6 6" stroke="#444" stroke-width="4"/></svg></div></div>
  <div class="pill right" style="left:410px;top:340px"><div class="ico"><svg width="24" height="24" viewBox="0 0 24 24"><circle cx="12" cy="7" r="5.5" fill="#444"/><path d="M2 24a10 10 0 0 1 20 0Z" fill="#444"/></svg></div>
    <div class="txt"><div class="ttl">Fokus</div>Der Fokus auf DS-GVO und EPVO gewinnt an Bedeutung. Wir sind Ihr Datenschutzpartner mit klarem Ziel.</div></div>
</section>

<!-- Seite 4 -->
<section class="page principles">
  <div class="abs principles-band"></div>
  <div class="photo" style="left:190px;top:0;width:250px;height:210px;opacity:.55" role="img" aria-label="Foto: Ritter mit Schild, halbtransparent im Hintergrund"></div>
  <div class="abs principles-title">PRAGMATISCH. SICHER. KOMPETENT!</div>

  <div class="pillar" style="left:29px">
    <svg width="88" height="96" viewBox="0 0 88 96"><path d="M44 4 L82 18 L82 52 Q82 78 44 92 Q6 78 6 52 L6 18 Z" fill="#fff" stroke="var(--green)" stroke-width="6"/><circle cx="44" cy="42" r="11" fill="#444"/><rect x="38" y="54" width="12" height="8" fill="#444"/></svg>
    <h3>Warum<br>Korvento?</h3>
    <div class="body">Wir rüsten Sie gegen Bedrohungen durch IT und Cyber Kriminalität sowie Datenklau und bieten die perfekte Beratung, ganz gleich ob DS-GVO oder EPVO! Durch extern geprüfte und zertifizierte Mitarbeiter.</div>
  </div>
  <div class="pillar" style="left:245px">
    <svg width="88" height="96" viewBox="0 0 88 96"><path d="M44 4 L82 18 L82 52 Q82 78 44 92 Q6 78 6 52 L6 18 Z" fill="#fff" stroke="var(--green)" stroke-width="6"/><circle cx="38" cy="46" r="10" fill="none" stroke="#444" stroke-width="6" stroke-dasharray="4 3"/><circle cx="54" cy="34" r="7" fill="none" stroke="#444" stroke-width="5" stroke-dasharray="3 2"/></svg>
    <h3>Unsere<br>Maßnahmen</h3>
    <div class="body">Passende Leistungspakete für jedes Unternehmen. Wir helfen Ihnen die neue DSGVO in Ihrem Unternehmen problemlos zu integrieren. Wir beraten sowohl kleine als auch mittelständische Unternehmen für eine optimale Umsetzung.</div>
  </div>
  <div class="pillar" style="left:456px">
    <svg width="88" height="96" viewBox="0 0 88 96"><path d="M44 4 L82 18 L82 52 Q82 78 44 92 Q6 78 6 52 L6 18 Z" fill="#fff" stroke="var(--green)" stroke-width="6"/><circle cx="42" cy="42" r="12" fill="none" stroke="#444" stroke-width="4"/><path d="M36 42l5 5 8-9" fill="none" stroke="#444" stroke-width="3"/><path d="M51 51l9 9" stroke="#444" stroke-width="5"/></svg>
    <h3>Unsere<br>Kontrolle</h3>
    <div class="body"><span class="lead">VERTRAUEN IST GUT –<br>KONTROLLE IST BESSER!</span><br>Durch externe Datenschutzbeauftragte gewinnen Sie das Vertrauen Ihrer Kunden und vermeiden unnötige Abmahnungen durch unseren Schutzschild-Plus (KOSPA).</div>
  </div>
</section>

<!-- Seite 5 -->
<section class="page culture">
  <div class="photo office" style="left:0;top:22px;width:415px;height:228px" role="img" aria-label="Foto: Hände an einem Laptop im Büro"></div>
  <div class="abs" style="left:28px;top:266px;width:370px">
    <h2 class="h-section" style="font-size:15px;color:var(--charcoal);margin-bottom:34px">Unsere Arbeiten</h2>
    <div class="cols">
      <div class="body"><p>Unsere Datenschutzexperten vereinbaren zunächst einen Termin mit Ihnen und kommen persönlich in Ihr Unternehmen.</p><p>Bei diesem detaillierten Datenschutz-Audit stellen wir den notwendigen Handlungsbedarf fest und begleiten Sie kompetent und pragmatisch bei den erforderlichen Maßnahmen. Wir sind sowohl intern als auch extern der erste Ansprechpartner,</p></div>
      <div class="body"><p>wenn es um Datenschutz und IT-Sicherheit geht.</p><p>Durch unsere Kundenplattform bieten wir Ihnen darüber hinaus zeit- und materialsparende Prozesse an. Einen ersten Check Ihrer Website werden wir zukünftig durch den Einsatz unserer geplanten <span style="color:var(--green)">Datenschutz-Applikation</span> vornehmen können. Somit kommt es nicht zu unnötigen Abmahnungen.</p></div>
    </div>
  </div>
  <div class="abs culture-side">
    <h2 class="h-section">Unsere Kultur</h2>
    <div class="body" style="font-size:7px">
      <p>Wir sind stets positiv eingestellt, gehen respektvoll miteinander um und arbeiten pragmatisch und hoch professionell.</p>
      <p>Teamarbeit &amp; persönliche Wertschätzung stehen bei uns an erster Stelle. Dazu zählt persönliche Leistung genauso wie Eigenständigkeit.</p>
      <p>Die Formel für eine <b>optimale Kundenbeziehung</b> ist der Erfolg, der sich aus Vertrauen und Problemverständnis zusammensetzt. Durch unsere Betreuung stehen Ihnen unsere gesamte Kompetenz und unser Expertenwissen für maximalen Erfolg zur Verfügung.</p>
    </div>
  </div>
  <div class="photo" style="left:440px;top:262px;width:215px;height:215px;background:linear-gradient(160deg,#3aaa35 0%,#a7adb3 40%,#5b6066 80%,#3aaa35 100%)" role="img" aria-label="Foto: stehender Ritter mit Schild und Schwert"></div>
</section>

<!-- Seite 6 -->
<section class="page packages">
  <div class="abs packages-band"></div>
  <div class="photo" style="left:200px;top:0;width:300px;height:280px;opacity:.5;background:linear-gradient(160deg,#8fcf8a,#2f6e2c 60%,#1f4f1d)" role="img" aria-label="Foto: Ritter mit Schild, grün eingefärbt"></div>
  <div class="abs packages-title">DAS FÜR SIE PASSENDE LEISTUNGSPAKET</div>

  <div class="pack" style="left:36px">
    <svg class="price" viewBox="0 0 56 56"><path d="M28 3 L52 12 L52 32 Q52 48 28 54 Q4 48 4 32 L4 12 Z" fill="#fff" stroke="var(--green)" stroke-width="4"/><text x="28" y="32" text-anchor="middle" font-family="Raleway,sans-serif" font-size="13" fill="#444">150€</text></svg>
    <div class="pack-label">Leistung S</div>
    <ul class="pack-list"><li>Einzelhandel</li><li>Gastronomie</li><li>Kfz-Betriebe</li><li>Handwerksbetriebe</li><li>Baugewerbe</li></ul>
  </div>
  <div class="pack" style="left:197px">
    <svg class="price" viewBox="0 0 56 56"><path d="M28 3 L52 12 L52 32 Q52 48 28 54 Q4 48 4 32 L4 12 Z" fill="#fff" stroke="var(--green)" stroke-width="4"/><text x="28" y="32" text-anchor="middle" font-family="Raleway,sans-serif" font-size="13" fill="#444">250€</text></svg>
    <div class="pack-label" style="background:var(--charcoal)">Leistung M</div>
    <ul class="pack-list"><li>Agenturen &amp; Makler</li><li>Werbebranche</li><li>Ärzte und Apotheker</li><li>Online Shops/E-Commerce</li><li>Transport &amp; Logistik</li></ul>
  </div>
  <div class="pack" style="left:357px">
    <svg class="price" viewBox="0 0 56 56"><path d="M28 3 L52 12 L52 32 Q52 48 28 54 Q4 48 4 32 L4 12 Z" fill="#fff" stroke="var(--green)" stroke-width="4"/><text x="28" y="32" text-anchor="middle" font-family="Raleway,sans-serif" font-size="13" fill="#444">350€</text></svg>
    <div class="pack-label">Leistung L</div>
    <ul class="pack-list"><li>Medizin und</li><li>Gesundheitswesen</li><li>Steuerberater</li><li>Medienunternehmen</li><li>Marketing</li></ul>
  </div>
  <div class="pack xl" style="left:518px">
    <svg class="price" viewBox="0 0 56 56"><path d="M28 3 L52 12 L52 32 Q52 48 28 54 Q4 48 4 32 L4 12 Z" fill="#fff" stroke="var(--green)" stroke-width="4"/><text x="28" y="32" text-anchor="middle" font-family="Raleway,sans-serif" font-size="13" fill="#444">500€</text></svg>
    <div class="pack-label">Leistung XL</div>
    <ul class="pack-list"><li>KMU's mit über 100 MA</li><li>Personal-Service</li><li>Finanzdienstleister</li><li>Produzierendes Gewerbe</li><li>Industrie</li></ul>
  </div>
</section>

<!-- Seite 7 -->
<section class="page audience">
  <div class="abs topbar" style="height:11px"></div>
  <h2 class="abs h-section" style="left:30px;top:38px;font-size:15px;color:var(--charcoal)">Wer braucht <b style="font-weight:400">Datenschutz?</b></h2>
  <div class="abs cta-tag">Worauf warten Sie?</div>
  <div class="abs cta-phone"><svg width="12" height="12" viewBox="0 0 12 12"><path d="M2 1l3 0 1 3-2 1a7 7 0 0 0 3 3l1-2 3 1 0 3c-6 0-9-3-9-9Z" fill="#fff"/></svg>0211 4470 18 52 0</div>

  <div class="abs audience-list">
    <div class="audience-item"><svg width="26" height="28" viewBox="0 0 26 28" style="flex:none"><path d="M13 2 L24 7 L24 16 Q24 23 13 26 Q2 23 2 16 L2 7 Z" fill="#fff" stroke="var(--green)" stroke-width="2"/><text x="13" y="19" text-anchor="middle" font-size="11" fill="#444" font-family="Raleway,sans-serif">1</text></svg><div>Privatrechtliche Organisationen und Firmen, aber auch Personen, die personenbezogene Daten verarbeiten (z.B.: Selbstständige, Produktions-, Handels- und Dienstleistungsunternehmen)</div></div>
    <div class="audience-item"><svg width="26" height="28" viewBox="0 0 26 28" style="flex:none"><path d="M13 2 L24 7 L24 16 Q24 23 13 26 Q2 23 2 16 L2 7 Z" fill="#fff" stroke="var(--green)" stroke-width="2"/><text x="13" y="19" text-anchor="middle" font-size="11" fill="#444" font-family="Raleway,sans-serif">2</text></svg><div>Sonstige Privatrechtliche Organisationen, deren Geschäftszweck die Verarbeitung personenbezogener Daten für Fremde ist (z.B.: Service-Rechenzentren oder Forschungseinrichtungen)</div></div>
    <div class="audience-item"><svg width="26" height="28" viewBox="0 0 26 28" style="flex:none"><path d="M13 2 L24 7 L24 16 Q24 23 13 26 Q2 23 2 16 L2 7 Z" fill="#fff" stroke="var(--green)" stroke-width="2"/><text x="13" y="19" text-anchor="middle" font-size="11" fill="#444" font-family="Raleway,sans-serif">3</text></svg><div>Öffentliche Stellen des Bundes und der Länder (z.B.: Bundesbehörden oder Kommunalverwaltungen)</div></div>
  </div>

  <div class="abs audience-bottom">
    <h2 class="h-section">Warum Korvento?</h2>
    <div class="body" style="font-size:7px">
      <p>Wir gewährleisten eine fehlerfreie Implementierung und Einhaltung eines ausreichenden Datenschutzes einschließlich der notwendigen technischen Voraussetzung.</p>
      <p>Zudem betreuen wir Sie kontinuierlich dahingehend, dass alle Abläufe den gesetzlichen Anforderungen gerecht werden und beugen somit aktiv Datenschutzverstößen vor.</p>
      <p>Unsere individualisierten Leistungspakete, die für jede Unternehmensgröße die optimale Betreuung bieten, sind auf Ihre speziellen Anforderungen abgestimmt.</p>
      <p>Sämtliche Leistungen sind auch individuell buchbar. Ein transparentes und faires Angebot ist für uns essenzieller Bestandteil einer kompetenten Beratung im Bereich Datenschutz und IT-Sicherheit.</p>
    </div>
  </div>
  <div class="photo" style="left:462px;top:84px;width:219px;height:400px" role="img" aria-label="Foto: Ritter mit grünem Schild, seitlich angeschnitten"></div>
</section>

</body>
</html>
```